Business cards and logo for kitchen and bath remodeling company

We want an elegant card but that calls attention something unique and when people see it they remember us. A log that we can use for our own. We are a kitchen and bathroom remodeling company. We are 3 partners staring the company we are located in seattle washington usa. We try to give the best experience and luxury look in our projects and we are looking to show that in our cards. I added a sample of a card I really like. I like the black and gold look but gray blue or green in a metallic look would look nice. I'm open to any color.

Target Market(s)

Home owners.

Industry/Entity Type

Construction

Contact Information for Business Card

Larchmont and Vey builders

Colors

Designer to choose colors to be used in the design.

Requirements
Must have
• Make a Logo
• Logo to be unique
• Name of company larchmont and vey builders
Nice to have
• Have a good color scheme
• Front design to connect with back of card

```html
<!DOCTYPE html>
<html lang="en">
<head>
<meta charset="utf-8">
<title>Larchmont &amp; Vey Builders — Business Cards</title>
<link href="https://fonts.googleapis.com/css2?family=Questrial&family=Handlee&display=swap" rel="stylesheet">
<style>
  :root {
    --canvas: #e9e9e9;
    --card-dark: #3b3838;
    --card-light: #d6d6d6;
    --teal: #1db8be;
    --teal-deep: #137c84;
    --white: #ffffff;
  }
  html, body {
    margin: 0;
    padding: 0;
    width: 1200px;
    height: 1136px;
    overflow: hidden;
    background: var(--canvas);
  }
  .sheet {
    position: relative;
    width: 1200px;
    height: 1136px;
  }
  .card {
    position: absolute;
    width: 540px;
    height: 309px;
    box-shadow: 0 6px 18px rgba(0,0,0,0.18);
    box-sizing: border-box;
  }
  .card-front {
    left: 40px;
    top: 70px;
    background: var(--card-dark);
    display: flex;
    flex-direction: column;
    align-items: center;
    justify-content: center;
  }
  .card-back {
    left: 620px;
    top: 70px;
    background: var(--card-light);
    padding: 62px 0 0 54px;
  }
  .brand-dot {
    display: block;
    width: 52px;
    height: 52px;
    border-radius: 50%;
    background: var(--teal-deep);
    margin: 0 auto 18px;
  }
  .wordmark {
    font-family: "Questrial", sans-serif;
    font-weight: 400;
    color: var(--teal);
    text-transform: uppercase;
    text-align: center;
    margin: 0;
  }
  .wordmark-main {
    display: block;
    font-size: 28px;
    letter-spacing: 0.26em;
    margin-right: -0.26em;
  }
  .wordmark-sub {
    display: block;
    font-size: 18px;
    letter-spacing: 0.42em;
    margin-right: -0.42em;
    margin-top: 6px;
  }
  .holder-name {
    font-family: "Handlee", cursive;
    font-size: 40px;
    color: var(--teal-deep);
    margin: 0 0 4px 60px;
    line-height: 1.1;
  }
  .name-rule {
    display: block;
    width: 420px;
    height: 2px;
    background: var(--teal);
    margin: 0 0 16px 0;
  }
  .contact {
    font-family: "Questrial", sans-serif;
    margin: 0 0 0 80px;
    line-height: 1.45;
  }
  .contact-phone {
    display: block;
    font-size: 20px;
    letter-spacing: 0.12em;
    color: var(--teal-deep);
  }
  .contact-email {
    display: block;
    font-size: 17px;
    letter-spacing: 0.1em;
    color: var(--teal);
  }
  .contact-web {
    display: block;
    font-family: "Questrial", sans-serif;
    font-size: 17px;
    letter-spacing: 0.1em;
    color: var(--teal-deep);
    margin: 26px 0 0 20px;
  }
  .logo-panel {
    position: absolute;
    left: 40px;
    top: 440px;
    width: 1120px;
    height: 640px;
    background: var(--white);
    display: flex;
    flex-direction: column;
    align-items: center;
    justify-content: center;
  }
  .logo-panel .brand-dot {
    width: 96px;
    height: 96px;
    margin-bottom: 30px;
  }
  .logo-panel .wordmark-main {
    font-size: 46px;
  }
  .logo-panel .wordmark-sub {
    font-size: 28px;
    margin-top: 10px;
  }
</style>
</head>
<body>
  <main class="sheet">
    <section class="card card-front" aria-label="Card front">
      <span class="brand-dot" aria-hidden="true"></span>
      <h1 class="wordmark">
        <span class="wordmark-main">Larchmont &amp; Vey</span>
        <span class="wordmark-sub">Builders</span>
      </h1>
    </section>

    <section class="card card-back" aria-label="Card back">
      <p class="holder-name">Marisol Ferreira</p>
      <span class="name-rule"></span>
      <p class="contact">
        <span class="contact-phone">206 55 41 907</span>
        <span class="contact-email">mferreira@mailbox.com</span>
      </p>
      <p class="contact-web">www.larchmontandvey</p>
    </section>

    <section class="logo-panel" aria-label="Brand logo">
      <span class="brand-dot" aria-hidden="true"></span>
      <p class="wordmark">
        <span class="wordmark-main">Larchmont &amp; Vey</span>
        <span class="wordmark-sub">Builders</span>
      </p>
    </section>
  </main>
</body>
</html>
```